Flyer DL double sided Design Project

Hi,

Our company Harbin Panels makes kitchen and wardrobe doors. I would like an attractive and sales focused artwork for a DL flyer for general promotional use to be printed and also emailed to customers. The flyer will be a double sided, full colour and gloss finish.

We would hand out this flyer to people wanting to replace their old kitchen doors with new ones. The flyer is aimed at the general public and the Do It Yourself market as we supply the doors only, we don't measure or install.

Text will be provided but here are some guidelines:

Headline: IS YOUR KITCHEN IN NEED OF A MAKEOVER? JUST REPLACE THE DOORS SAVING YOU THOUSANDS OF $$$

This month’s special offers: Online orders only. ORDER NOW! (icon)

5 reasons to replace kitchen doors compared to a full kitchen renovation:
1. Its cheaper text, text, text
2. It's quicker text, text, text
3. It's easier text, text, text
4. It's less hassle and mess text, text, text
5. It's less wastage text, text, text

I can also provide a few high quality images of kitchens.

Reason: I won't be available to provide feedback on the design and finalise it within the deadline date. Regards, Marcia

Reason: I don't have the wording and final image today. I will be able to finalise early next week.

DO IT YOURSELF - DIY
This is mainly aimed at people who want to replace their kitchen doors themselves. People interested in improving the value of their home and saving a lot of money on their kitchen renovation.
Home owners - usually adults in the 30-50 year age bracket.

• List our website www.harbinpanels.com.au
List our email address: sales@harbinpanels.com.au
We do not measure or install. We can give quotes to customers who email a list of door sizes to us. For example: Headline: Get a quote now! Smaller print: Download a quote form (from our website www.harbinpanels.com.au) and send your door sizes for a quote today!
• Promotion: Order now and receive free delivery (on orders over $1000). Sydney metro area. Limited time only.
I like the design done by Quillmark42 with "We do wardrobe doors too" on the back of the flyer.
Delivery to your door anywhere in Australia.

```html
<!DOCTYPE html>
<html lang="en">
<head>
<meta charset="utf-8">
<title>Harbin Panels – DL Flyer</title>
<link rel="stylesheet" href="https://fonts.googleapis.com/css2?family=Arimo:wght@400;700&family=Tinos:wght@700&display=swap">
<style>
  :root {
    --stage: #2a1d16;
    --paper: #ffffff;
    --ink: #1c1c1c;
    --orange: #f9bd54;
    --orange-soft: #fde6b6;
    --tagline: #f4a53a;
    --glass-teal: #3f8f98;
    --glass-grey: #b9c3cc;
    --glass-blue: #a9c4e6;
    --door-red: #c42a34;
    --door-blue: #3f6a99;
    --badge-blue: #1d4a94;
  }
  * { box-sizing: border-box; margin: 0; padding: 0; }
  html, body { width: 1200px; height: 900px; overflow: hidden; }
  body {
    background: var(--stage);
    font-family: "Arimo", Arial, sans-serif;
    color: var(--ink);
    position: relative;
  }
  .flyer {
    position: absolute;
    top: 38px;
    width: 388px;
    height: 824px;
    background: var(--paper);
    overflow: hidden;
  }
  .flyer--back { left: 160px; }
  .flyer--front { left: 653px; }

  /* Back side */
  .back-header {
    position: absolute; inset: 0 0 auto 0; height: 230px;
    background: linear-gradient(115deg, var(--glass-teal) 0%, var(--glass-grey) 35%, var(--glass-blue) 70%, #dfe8f4 100%);
  }
  .back-title {
    position: absolute; top: 44px; left: 108px;
    font-size: 38px; font-weight: 400; line-height: 1; white-space: nowrap;
    color: #fff; text-shadow: 0 1px 3px rgba(0,0,0,.35);
  }
  .back-tagline {
    position: absolute; top: 94px; left: 110px;
    font-size: 20px; line-height: 1; white-space: nowrap; color: var(--tagline);
  }
  .badge {
    position: absolute; top: 118px; left: 14px; width: 84px; height: 84px;
    border-radius: 50%; background: var(--badge-blue); border: 4px solid #fff;
    box-shadow: 0 1px 4px rgba(0,0,0,.3);
  }
  .badge::after {
    content: ""; position: absolute; inset: 10px; border-radius: 50%; background: #fff;
  }
  .back-body { position: absolute; top: 240px; left: 0; right: 0; text-align: center; }
  .headline-save { font-weight: 700; font-size: 21px; line-height: 1.2; }
  .reasons-intro { margin-top: 22px; font-size: 17px; line-height: 1.2; }
  .reasons {
    list-style: none; margin: 14px 0 0 40px; text-align: left;
    font-size: 20px; line-height: 1.2;
  }
  .quote-title { margin-top: 24px; font-family: "Tinos", "Times New Roman", serif; font-weight: 700; font-size: 30px; }
  .quote-text { font-family: "Tinos", "Times New Roman", serif; font-weight: 700; font-size: 12.5px; line-height: 1.35; }
  .order-now { margin-top: 14px; font-weight: 700; font-size: 20px; }
  .promo {
    position: absolute; left: 0; right: 0; bottom: 0; height: 180px;
    background: var(--orange); text-align: center; padding-top: 12px;
  }
  .promo-title { font-weight: 700; font-size: 24px; }
  .promo-text { font-size: 13.5px; line-height: 1.3; margin-top: 2px; }
  .promo-strong { font-weight: 700; font-size: 13.5px; margin-top: 4px; }
  .promo-note { font-size: 10px; margin-top: 4px; }
  .web { font-weight: 700; font-size: 16px; letter-spacing: 4px; }
  .promo .web { margin-top: 8px; }

  /* Front side */
  .front-header {
    position: absolute; inset: 0 0 auto 0; height: 216px;
    background: linear-gradient(165deg, #f7b548 0%, #fbcf7c 45%, var(--orange-soft) 80%, #fff 100%);
  }
  .brand {
    position: absolute; top: 62px; left: 16px; width: 132px; text-align: center;
  }
  .brand-mark { display: block; width: 26px; height: 26px; margin: 0 auto 8px; background: #fff; }
  .brand-name { font-weight: 700; font-size: 26px; line-height: 1.05; color: #1c1c1c; }
  .collection { position: absolute; top: 76px; left: 160px; right: 10px; text-align: center; color: #fff; }
  .collection-lead { font-weight: 700; font-size: 40px; line-height: 1; }
  .collection-sub { font-size: 28px; margin-top: 10px; }
  .offers-label { position: absolute; top: 252px; left: 0; right: 0; text-align: center; font-weight: 700; font-size: 20px; }
  .makeover {
    position: absolute; top: 316px; left: 0; right: 0; text-align: center;
    font-weight: 700; font-size: 30px; line-height: 1.25;
  }
  .door-art { position: absolute; left: 0; top: 370px; }
  .contact { position: absolute; top: 594px; left: 0; right: 0; text-align: center; font-weight: 700; }
  .contact-name { font-size: 21px; }
  .contact-line { font-size: 16px; line-height: 1.25; }
  .contact-phones { margin-top: 42px; }
  .flyer--front .web { position: absolute; bottom: 14px; left: 0; right: 0; text-align: center; }
</style>
</head>
<body>

<section class="flyer flyer--back" aria-label="Flyer back side">
  <div class="back-header" role="img" aria-label="Glass wardrobe door panels in teal, grey and blue"></div>
  <h1 class="back-title">Harbin Panels</h1>
  <p class="back-tagline">We do wardrobe doors too</p>
  <div class="badge" role="img" aria-label="Quality and service badge"></div>

  <div class="back-body">
    <h2 class="headline-save">JUST REPLACE THE DOORS<br>SAVING YOU THOUSANDS OF $$$</h2>
    <p class="reasons-intro">5 Reasons to replace kitchen doors<br>compared to a full kitchen renovation:</p>
    <ol class="reasons">
      <li>1. Its cheaper</li>
      <li>2. Its quicker</li>
      <li>3. Its easier</li>
      <li>4. Its less hassle and mess</li>
      <li>5. Its less wastage</li>
    </ol>
    <p class="quote-title">Get a quote now!</p>
    <p class="quote-text">Download a quote form from our website<br>www.harbinpanels.com.au<br>and send your door sizes for a quote today!</p>
    <p class="order-now">Online orders only. ORDER NOW!</p>
  </div>

  <div class="promo">
    <p class="promo-title">Promotion</p>
    <p class="promo-text">Order now and receive free delivery<br>(on orders over $1000). Sydney metro area.<br>Limited time only.</p>
    <p class="promo-strong">Delivery to your door anywhere in Australia.</p>
    <p class="promo-note">*We do not measure or install.</p>
    <p class="web">www.harbinpanels.com.au</p>
  </div>
</section>

<section class="flyer flyer--front" aria-label="Flyer front side">
  <div class="front-header"></div>
  <div class="brand">
    <span class="brand-mark"></span>
    <p class="brand-name">Harbin Panels</p>
  </div>
  <div class="collection">
    <p class="collection-lead">ultimate</p>
    <p class="collection-sub">door collection</p>
  </div>

  <svg class="door-art" width="388" height="410" viewBox="0 0 388 410" role="img" aria-label="Blue and red kitchen cabinet doors">
    <polygon points="0,20 150,150 0,330" fill="var(--door-blue)"/>
    <polygon points="250,170 388,60 388,330" fill="var(--door-red)"/>
  </svg>

  <p class="offers-label">This month’s special offers:</p>
  <h2 class="makeover">IS YOUR KITCHEN<br>IN NEED<br>OF A<br>MAKEOVER?</h2>

  <div class="contact">
    <p class="contact-name">HARBIN PANELS</p>
    <p class="contact-line">14 Calder Road,<br>Kellyville Ridge NSW 2155</p>
    <div class="contact-phones">
      <p class="contact-line">Ph 9610 3820</p>
      <p class="contact-line">Fax 9610 3821</p>
      <p class="contact-line">Email sales@harbinpanels.com.au</p>
    </div>
  </div>
  <p class="web">www.harbinpanels.com.au</p>
</section>

</body>
</html>
```